BHSC Business cards

We are an established dental practice that is looking for new business cards to match our new logo. We are looking for something unique and sophisticated.
BRIEF: Colours are black, silver and white. Include the company name, logo (including “Pelwick Heath Dental Care”) and phone number “03 9415 2876”.
Front - Include the company name, logo (including “Pelwick Heath Dental Care”) and phone number “03 9415 2876”.
Back - Include the company name,  “Pelwick Heath Dental Care”, phone number “03 9415 2876”. address "64A Tindle Street, Pelwick Heath, Vic 3187", "Email reception@pelwickheathdentalcare.com.au", the Dentist Name " Dr ................................"  Your next appointment "Day, date and time(am/pm)".  3 lines for 3 appointments please, and at the bottom "IF UNABLE TO KEEP THIS APPOINTMENT 48 HOURS NOTICE IS REQUIRED."
Try and be creative and different with the design, i've added an image for inspiration

Target Market(s)
ALL in need of dental
Industry/Entity Type
Dental Clinic
Look and feel
Each slider illustrates characteristics of the customer's brand and the style your logo design should communicate.

```html
<!DOCTYPE html>
<html lang="en">
<head>
<meta charset="utf-8">
<title>Pelwick Heath Dental Care — Business Cards</title>
<link href="https://fonts.googleapis.com/css2?family=Arimo:wght@400;700&family=Archivo+Black&display=swap" rel="stylesheet">
<style>
  :root {
    --backdrop: #1c1c1c;
    --card: #ffffff;
    --ink: #1a1818;
    --band: #231f20;
    --band-text: #ffffff;
    --rule: #555555;
  }
  * { box-sizing: border-box; margin: 0; padding: 0; }
  html, body {
    width: 1200px; height: 900px; overflow: hidden;
    background: var(--backdrop);
    font-family: "Arimo", Arial, sans-serif;
    color: var(--ink);
  }
  .canvas {
    position: relative; width: 1200px; height: 900px;
    display: flex; flex-direction: column; align-items: center; justify-content: center; gap: 46px;
  }
  .card {
    position: relative; width: 620px; height: 354px;
    background: var(--card);
    box-shadow: 0 14px 30px rgba(0,0,0,.6);
    overflow: hidden;
  }
  .band {
    position: absolute; left: 0; right: 0; bottom: 0;
    background: var(--band); color: var(--band-text);
    display: flex; align-items: center; justify-content: center;
  }

  /* Front */
  .front .lockup {
    position: absolute; top: 118px; left: 0; right: 0;
    display: flex; align-items: center; justify-content: center; gap: 16px;
  }
  .mark-circle {
    width: 70px; height: 70px; border-radius: 50%;
    border: 4px solid var(--ink); flex: none;
  }
  .brand-name {
    font-family: "Arimo", Arial, sans-serif; font-weight: 700;
    font-size: 24px; letter-spacing: 2px; line-height: 1.2;
    text-transform: uppercase; color: var(--ink);
  }
  .front .tagline-phone {
    position: absolute; top: 204px; left: 0; right: 0; text-align: center;
    font-size: 15px; letter-spacing: 3px; font-weight: 700;
  }
  .front .band { height: 64px; }
  .front .band-phone {
    font-family: "Archivo Black", Arial, sans-serif;
    font-size: 28px; letter-spacing: 4px;
  }

  /* Back */
  .back .mark-circle {
    position: absolute; top: 26px; left: 40px; width: 84px; height: 84px;
  }
  .back .contact {
    position: absolute; top: 40px; left: 150px;
    font-size: 15px; line-height: 1.35;
  }
  .back .dentist {
    position: absolute; top: 128px; left: 120px;
    font-size: 16px; letter-spacing: .5px;
  }
  .back .appointments {
    position: absolute; top: 162px; left: 40px; right: 40px;
    display: flex; flex-direction: column; gap: 16px;
  }
  .appt-row {
    display: flex; align-items: flex-end; font-size: 16px; letter-spacing: .5px;
  }
  .fill-line {
    flex: 1; border-bottom: 1px solid var(--rule); height: 14px; margin: 0 6px;
  }
  .back .band { height: 52px; }
  .notice { font-size: 13px; letter-spacing: .8px; }
</style>
</head>
<body>
<main class="canvas">
  <section class="card front" aria-label="Card front">
    <div class="lockup">
      <span class="mark-circle"></span>
      <div class="brand-name">Pelwick Heath<br>Dental Care</div>
    </div>
    <p class="tagline-phone">03 9415 2876</p>
    <div class="band"><span class="band-phone">03 9415 2876</span></div>
  </section>

  <section class="card back" aria-label="Card back">
    <span class="mark-circle"></span>
    <div class="contact">
      <p>03 9415 2876</p>
      <p>reception@pelwickheathdentalcare.com.au</p>
      <p>64A Tindle Street, Pelwick Heath, Vic 3187</p>
    </div>
    <p class="dentist">THE DENTIST NAME " DR ................................"</p>
    <div class="appointments">
      <div class="appt-row">DATE<span class="fill-line"></span>AT<span class="fill-line"></span>AM/PM</div>
      <div class="appt-row">DATE<span class="fill-line"></span>AT<span class="fill-line"></span>AM/PM</div>
      <div class="appt-row">DATE<span class="fill-line"></span>AT<span class="fill-line"></span>AM/PM</div>
    </div>
    <div class="band"><span class="notice">IF UNABLE TO KEEP THIS APPOINTMENT 48 HOURS NOTICE IS REQUIRED</span></div>
  </section>
</main>
</body>
</html>
```